KORBALT

The business want a professional looking business card. We have a scetch we will add but want the extra upgrade, and would like more suggestions for variations of our business cards.

```html
<!DOCTYPE html>
<html lang="en">
<head>
<meta charset="utf-8">
<title>KORBALT Business Card</title>
<link href="https://fonts.googleapis.com/css2?family=Montserrat:wght@400;500;600;700&display=swap" rel="stylesheet">
<style>
  :root {
    --backdrop: #cfd0d2;
    --bronze-dark: #6f5426;
    --bronze-mid: #8d6a31;
    --bronze-light: #a88238;
    --gold: #e2bf5c;
    --gold-soft: #ead089;
    --cream: #fbf0d2;
    --paper: #fffdf7;
    --ink: #4a3318;
  }
  * { margin: 0; padding: 0; box-sizing: border-box; }
  html, body { width: 1200px; height: 900px; overflow: hidden; }
  body {
    background: var(--backdrop);
    font-family: "Montserrat", sans-serif;
    position: relative;
  }
  .card {
    position: absolute;
    top: 170px;
    width: 330px;
    height: 560px;
    overflow: hidden;
    box-shadow: 0 18px 40px rgba(0,0,0,0.18);
  }
  .card--front {
    left: 225px;
    background: linear-gradient(160deg, var(--bronze-dark) 0%, var(--bronze-mid) 55%, var(--bronze-light) 100%);
  }
  .card--back {
    left: 645px;
    background: linear-gradient(150deg, var(--cream) 0%, var(--paper) 60%, #ffffff 100%);
  }

  /* Front */
  .front-brand {
    position: absolute;
    left: 0; right: 0; top: 236px;
    text-align: center;
    color: var(--gold);
  }
  .front-brand__name {
    display: inline-flex;
    align-items: center;
    gap: 10px;
    font-size: 34px;
    font-weight: 600;
    letter-spacing: 6px;
  }
  .front-brand__dot {
    width: 12px; height: 12px;
    border-radius: 50%;
    background: var(--gold);
  }
  .front-brand__since {
    margin-top: 10px;
    font-size: 11px;
    font-weight: 600;
    letter-spacing: 5px;
  }

  /* Back */
  .holder {
    position: absolute;
    left: 30px; top: 34px;
    width: 230px;
  }
  .holder__name {
    font-size: 15px;
    font-weight: 500;
    color: var(--ink);
    letter-spacing: 0.5px;
    padding-bottom: 8px;
    border-bottom: 1px solid var(--gold);
  }
  .holder__role {
    margin-top: 8px;
    font-size: 40px;
    font-weight: 600;
    line-height: 0.95;
    color: var(--ink);
    letter-spacing: -1px;
  }
  .back-brand {
    position: absolute;
    left: 30px; top: 236px;
    display: flex;
    align-items: center;
    gap: 8px;
    font-size: 24px;
    font-weight: 600;
    letter-spacing: 4px;
    color: var(--gold);
  }
  .back-brand__dot {
    width: 10px; height: 10px;
    border-radius: 50%;
    background: var(--gold);
  }
  .contact {
    position: absolute;
    left: 30px; top: 380px;
    width: 200px;
    color: var(--ink);
  }
  .contact__icons {
    display: flex;
    gap: 12px;
    padding-bottom: 8px;
    margin-bottom: 8px;
    border-bottom: 1px solid var(--gold);
  }
  .contact__icons svg { width: 16px; height: 16px; fill: var(--ink); }
  .contact__line {
    font-size: 12.5px;
    font-weight: 500;
    line-height: 1.6;
  }
  .back-wordmark {
    position: absolute;
    right: -6px; bottom: 0;
    transform-origin: right bottom;
    transform: rotate(-90deg) translateX(100%);
    font-size: 86px;
    font-weight: 600;
    letter-spacing: 6px;
    line-height: 0.8;
    color: var(--gold);
    white-space: nowrap;
  }
</style>
</head>
<body>
  <section class="card card--front">
    <div class="front-brand">
      <div class="front-brand__name"><span class="front-brand__dot"></span>KORBALT</div>
      <div class="front-brand__since">SINCE 2026</div>
    </div>
  </section>

  <section class="card card--back">
    <div class="holder">
      <div class="holder__name">Anders Holm Vikersund</div>
      <div class="holder__role">CEO &amp;<br>Founder</div>
    </div>

    <div class="back-brand"><span class="back-brand__dot"></span>KORBALT</div>

    <div class="contact">
      <div class="contact__icons">
        <svg viewBox="0 0 24 24" aria-label="Phone"><path d="M6.6 10.8a15 15 0 0 0 6.6 6.6l2.2-2.2c.3-.3.7-.4 1-.2 1.1.4 2.3.6 3.6.6.6 0 1 .4 1 1V20c0 .6-.4 1-1 1A17 17 0 0 1 3 4c0-.6.4-1 1-1h3.5c.6 0 1 .4 1 1 0 1.3.2 2.5.6 3.6.1.3 0 .7-.2 1z"/></svg>
        <svg viewBox="0 0 24 24" aria-label="Email"><path d="M2 5h20v14H2z M3 6l9 7 9-7" fill="var(--ink)"/><path d="M3 6l9 7 9-7" stroke="var(--paper)" stroke-width="1.6" fill="none"/></svg>
        <svg viewBox="0 0 24 24" aria-label="Website"><circle cx="12" cy="12" r="10"/><path d="M2 12h20M12 2c3 3 3 17 0 20M12 2c-3 3-3 17 0 20" stroke="var(--paper)" stroke-width="1.5" fill="none"/></svg>
      </div>
      <div class="contact__line">00 47 55 01 23 45</div>
      <div class="contact__line">korbalt.llc@postmail.com</div>
      <div class="contact__line">www.korbalt.llc</div>
    </div>

    <div class="back-wordmark">KORBALT</div>
  </section>
</body>
</html>
```